Microlight Aircraft Website Project

Need a website designed, or at least a template made, that my web programmer can work with here. We are a new manufacturer of microlight aircraft & powered hang gliders. Our company name is Brisk Fern. We manufacture portable utility aircraft in the Light Sport category (formerly known as Ultralights or Microlights). Our particular design is a 2-seat powered hang glider and caters to those who want to go explore the backcountry. We are not necessarily aviation nuts, but more into the development of a flying utility vehicle for extreme exploration and expeditions. We have been importing these aircraft from 3 countries for 15 years and have supplied over 200 expedition-quality aircraft world-wide. We are now manufacturing here in the US.

Industry/Entity Type

Manufacturer

Coding

Coded - Design and coding required

```html
<!DOCTYPE html>
<html lang="en">
<head>
<meta charset="utf-8">
<title>Brisk Fern — Microlight Aircraft</title>
<link rel="stylesheet" href="https://fonts.googleapis.com/css2?family=Ubuntu:wght@400;500;700&family=Open+Sans:wght@400;600;700&display=swap">
<style>
:root{
  --blue:#3c5fb4;
  --blue-dark:#2f4d98;
  --navy:#223a78;
  --sky:#4aa3dc;
  --accent:#f2a91c;
  --ink:#2b3440;
  --muted:#8a929c;
  --line:#dfe3e8;
  --panel:#f1f3f6;
  --white:#ffffff;
}
*{margin:0;padding:0;box-sizing:border-box}
html,body{width:1200px;height:4905px;overflow:hidden;background:var(--white)}
body{font-family:"Open Sans",Arial,sans-serif;color:var(--ink);position:relative}
h1,h2,h3,h4,.stat-num,.nav a,.logo-name{font-family:"Ubuntu","Open Sans",sans-serif}
.abs{position:absolute}

/* top bar */
.topbar{position:absolute;top:0;left:0;width:1200px;height:34px;border-bottom:1px solid var(--line);font-size:12px;color:var(--sky)}
.topbar .call{position:absolute;left:130px;top:9px}
.topbar .links{position:absolute;left:680px;top:9px;display:flex;gap:22px}
.topbar .social{position:absolute;left:955px;top:10px;display:flex;gap:12px}
.topbar .social span{width:11px;height:11px;border-radius:50%;background:var(--sky)}

/* header */
.header{position:absolute;top:34px;left:0;width:1200px;height:140px}
.logo{position:absolute;left:110px;top:20px;display:flex;flex-direction:column;align-items:center;gap:8px}
.logo-mark{width:46px;height:46px;border-radius:50%;background:var(--blue)}
.logo-name{font-size:30px;font-weight:700;color:var(--blue);letter-spacing:.5px}
.nav{position:absolute;left:395px;top:64px;display:flex;gap:30px;font-size:13px;font-weight:700}
.nav a{color:var(--ink);text-decoration:none}
.nav a.active{border-bottom:2px solid var(--ink);padding-bottom:6px}
.search{position:absolute;left:1044px;top:62px}

/* hero */
.hero{position:absolute;top:180px;left:0;width:1200px;height:640px;background:linear-gradient(180deg,#6fb3e8 0%,#3f93d6 55%,#2f79c2 100%)}
.hero-photo{position:absolute;inset:0}
.hero h1{position:absolute;top:125px;left:0;width:1200px;text-align:center;color:var(--white);font-size:38px;font-weight:700;line-height:1.35}
.hero .arrow{position:absolute;top:300px;width:42px;height:42px;border-radius:50%;background:rgba(255,255,255,.85)}
.hero .btn{position:absolute;left:505px;top:405px;width:190px;height:56px;border:2px solid var(--white);color:var(--white);font-size:14px;font-weight:700;text-align:center;line-height:52px;background:rgba(47,77,152,.25)}
.tabs{position:absolute;top:745px;left:170px;width:860px;height:75px}
.tabs svg{position:absolute;inset:0}
.tab-label{position:absolute;top:25px;font-family:"Ubuntu",sans-serif;font-weight:700;font-size:18px;display:flex;align-items:center;gap:10px}
.tab-label i{width:24px;height:24px;border-radius:50%;border:2px solid var(--ink);display:block}

/* about */
.about{position:absolute;top:820px;left:0;width:1200px;height:455px;background:var(--blue);color:var(--white)}
.about h2{font-size:42px;font-weight:700;position:absolute;left:130px;top:32px}
.about h3{font-size:26px;font-weight:700;position:absolute;left:455px;top:32px}
.about p{font-size:13px;line-height:1.6}
.about .col-left{position:absolute;left:130px;top:100px;width:290px}
.about .col-left p+p{margin-top:28px}
.about .col-right{position:absolute;left:455px;top:100px;width:610px}
.about .illus{position:absolute;left:630px;top:210px;width:185px;height:170px;border-radius:6px;background:linear-gradient(135deg,#d9a47a,#6e4b3a)}

/* experts */
.experts h2{position:absolute;top:1375px;left:0;width:1200px;text-align:center;font-size:40px;font-weight:700;color:var(--ink)}
.feature{position:absolute;width:280px}
.feature .tick{position:absolute;left:0;top:0;width:28px;height:28px}
.feature h4{margin-left:48px;font-size:15px;font-weight:700;color:var(--ink)}
.feature p{margin-left:48px;margin-top:8px;font-size:13px;line-height:1.55;color:var(--muted)}
.experts .rule{position:absolute;top:1895px;left:130px;width:940px;height:1px;background:var(--line)}

/* timeline */
.timeline{position:absolute;top:1980px;left:0;width:1200px;height:720px;background:var(--panel)}
.timeline h2{position:absolute;top:18px;left:0;width:1200px;text-align:center;font-size:40px;font-weight:700}
.timeline .month{position:absolute;top:100px;font-size:13px;color:var(--muted)}
.timeline .track{position:absolute;top:130px;left:0;width:1200px;height:50px}
.tl-card{position:absolute;top:240px;width:230px;height:235px;background:var(--white);border:1px solid var(--line)}
.tl-card .pic{width:130px;height:70px;margin:30px auto 0;border-radius:4px}
.tl-card h4{text-align:center;margin-top:22px;font-size:15px;font-weight:700}
.tl-card p{text-align:center;font-size:11px;line-height:1.5;color:var(--muted);padding:8px 14px 0}
.timeline .pager{position:absolute;top:540px;width:52px;height:52px;border-radius:50%;background:#c9cdd3}

/* news */
.news h2{position:absolute;top:2790px;left:0;width:1200px;text-align:center;font-size:40px;font-weight:700}
.post{position:absolute;top:2915px;width:210px}
.post .pic{height:145px;background:linear-gradient(180deg,#7fb4e4,#3d5f8a 70%,#6a6154)}
.post h3{margin-top:22px;font-size:21px;font-weight:700;line-height:1.2;text-transform:uppercase}
.post p{margin-top:14px;font-size:13px;line-height:1.6;color:var(--muted)}
.post .more{display:block;margin-top:14px;font-size:11px;font-weight:700;color:var(--accent)}

/* stats */
.stats .rule{position:absolute;top:3418px;left:130px;width:940px;height:10px}
.stat{position:absolute;top:3500px;width:165px;text-align:center}
.stat-num{font-size:62px;font-weight:700;color:var(--ink);line-height:1}
.stat-label{display:inline-block;margin-top:12px;padding:7px 12px;background:var(--sky);color:var(--white);font-size:10px;font-weight:700;text-transform:uppercase;min-width:120px}

/* clients */
.clients h2{position:absolute;top:3810px;left:0;width:1200px;text-align:center;font-size:40px;font-weight:700}
.client{position:absolute;top:3925px;width:78px;height:78px;border-radius:50%;background:#d7dade}

/* contact */
.contact{position:absolute;top:4090px;left:0;width:1200px;height:750px;background:var(--blue);color:var(--white)}
.contact .vline{position:absolute;left:440px;top:0;width:2px;height:330px;background:var(--white)}
.contact .dot{position:absolute;left:432px;top:322px;width:18px;height:18px;border-radius:50%;border:2px solid var(--white);background:var(--blue)}
.contact h2{position:absolute;left:130px;top:178px;font-size:36px;font-weight:700}
.contact .addr{position:absolute;left:130px;top:258px;font-size:12px;line-height:1.6}
.contact .addr b{font-weight:700}
.contact .reach{position:absolute;left:130px;top:640px;font-size:11px;line-height:1.7}
.contact .social{position:absolute;left:130px;top:692px;display:flex;gap:8px}
.contact .social span{width:26px;height:26px;background:var(--sky)}
.contact .note{position:absolute;left:535px;top:88px;font-size:13px}
.field{position:absolute;left:535px;width:465px;height:48px;border:1px solid rgba(255,255,255,.75);font-size:13px;padding:15px 20px;color:rgba(255,255,255,.85)}
.field.msg{height:150px}
.send{position:absolute;left:535px;top:508px;width:465px;height:52px;background:var(--navy);font-size:13px;font-weight:700;padding:17px 30px}
.send svg{position:absolute;right:20px;top:17px}

/* footer */
.footer{position:absolute;top:4840px;left:0;width:1200px;height:65px;background:var(--blue-dark);color:rgba(255,255,255,.85);font-size:12px;text-align:center;line-height:65px}
.footer b{color:var(--white);font-weight:600}
</style>
</head>
<body>

<div class="topbar">
  <span class="call">Call Us Now: 800 555 0142</span>
  <span class="links"><span>Request A Quote</span><span>Contact Us</span><span>Log In</span></span>
  <span class="social"><span></span><span></span><span></span><span></span></span>
</div>

<header class="header">
  <div class="logo"><span class="logo-mark"></span><span class="logo-name">BRISK FERN</span></div>
  <nav class="nav">
    <a class="active">HOME</a><a>AIRCRAFT FOR SALE</a><a>SERVICES</a><a>BLOG</a><a>CONTACT</a><a>REQUEST A QUOTE</a>
  </nav>
  <svg class="search" width="16" height="16" viewBox="0 0 16 16"><circle cx="6.5" cy="6.5" r="5" fill="none" stroke="#2b3440" stroke-width="2"/><line x1="10.5" y1="10.5" x2="15" y2="15" stroke="#2b3440" stroke-width="2"/></svg>
</header>

<section class="hero">
  <div class="hero-photo" role="img" aria-label="Powered hang glider flying across a bright blue sky with soft clouds"></div>
  <h1>LARGE ENOUGH TO HANDLE,<br>SMALL ENOUGH TO CARE</h1>
  <span class="arrow" style="left:28px"></span>
  <span class="arrow" style="left:1130px"></span>
  <div class="btn">READ MORE</div>
  <div class="tabs">
    <svg width="860" height="75" viewBox="0 0 860 75">
      <polygon points="20,0 290,0 290,75 0,75" fill="#fff"/>
      <polygon points="570,0 840,0 860,75 570,75" fill="#fff"/>
      <polygon points="290,0 570,0 570,75 290,75" fill="#3c5fb4"/>
    </svg>
    <span class="tab-label" style="left:95px;color:#4aa3dc"><i style="border-color:#2b3440"></i>Ultralights</span>
    <span class="tab-label" style="left:375px;color:#fff">BRISK FERN</span>
    <span class="tab-label" style="left:630px;color:#4aa3dc"><i></i>Microlights</span>
  </div>
</section>

<section class="about">
  <h2>ABOUT US</h2>
  <h3>MANUFACTURER</h3>
  <div class="col-left">
    <p>We are a new manufacturer of microlight aircraft &amp; powered hang gliders. Our company name is Brisk Fern. We manufacture portable utility aircraft in the Light Sport category (formerly known as Ultralights or Microlights).</p>
    <p>We are a new manufacturer of microlight aircraft &amp; powered hang gliders. Our company name is Brisk Fern. We manufacture portable utility aircraft in the Light Sport category (formerly known as Ultralights or Microlights).</p>
  </div>
  <div class="col-right">
    <p>We are a new manufacturer of microlight aircraft &amp; powered hang gliders. Our company name is Brisk Fern. We manufacture portable utility aircraft in the Light Sport category (formerly known as Ultralights or Microlights).</p>
  </div>
  <div class="illus" role="img" aria-label="Illustration of the manufacturing plant building"></div>
</section>

<section class="experts">
  <h2>OUR EXPERTS MEAN BUSINESS</h2>
  <div class="feature" style="left:130px;top:1500px">
    <svg class="tick" viewBox="0 0 28 28"><rect x="1" y="1" width="26" height="26" fill="none" stroke="#3c5fb4" stroke-width="2"/><path d="M7 14l5 5 10-11" fill="none" stroke="#3c5fb4" stroke-width="3"/></svg>
    <h4>15 YEARS</h4><p>We have 15 years of experience in this activity.</p>
  </div>
  <div class="feature" style="left:455px;top:1500px">
    <svg class="tick" viewBox="0 0 28 28"><rect x="1" y="1" width="26" height="26" fill="none" stroke="#3c5fb4" stroke-width="2"/><path d="M7 14l5 5 10-11" fill="none" stroke="#3c5fb4" stroke-width="3"/></svg>
    <h4>BUSINESS AVIATION</h4><p>All our owners are pilots, we understand the complexity of the Business Aviation world better than anybody.</p>
  </div>
  <div class="feature" style="left:780px;top:1500px">
    <svg class="tick" viewBox="0 0 28 28"><rect x="1" y="1" width="26" height="26" fill="none" stroke="#3c5fb4" stroke-width="2"/><path d="M7 14l5 5 10-11" fill="none" stroke="#3c5fb4" stroke-width="3"/></svg>
    <h4>WORLD MARKET</h4><p>We are in constant contact with the World Market and its daily moves.</p>
  </div>
  <div class="feature" style="left:130px;top:1685px">
    <svg class="tick" viewBox="0 0 28 28"><rect x="1" y="1" width="26" height="26" fill="none" stroke="#3c5fb4" stroke-width="2"/><path d="M7 14l5 5 10-11" fill="none" stroke="#3c5fb4" stroke-width="3"/></svg>
    <h4>TURN KEY SOLUTIONS</h4><p>We offer turn-key solutions, we take care of the commercial, technical, administrative, and legal side of the transaction.</p>
  </div>
  <div class="feature" style="left:455px;top:1685px">
    <svg class="tick" viewBox="0 0 28 28"><rect x="1" y="1" width="26" height="26" fill="none" stroke="#3c5fb4" stroke-width="2"/><path d="M7 14l5 5 10-11" fill="none" stroke="#3c5fb4" stroke-width="3"/></svg>
    <h4>CONCENTRATE</h4><p>You can concentrate on your business while we concentrate on your aircraft.</p>
  </div>
  <div class="feature" style="left:780px;top:1685px">
    <svg class="tick" viewBox="0 0 28 28"><rect x="1" y="1" width="26" height="26" fill="none" stroke="#3c5fb4" stroke-width="2"/><path d="M7 14l5 5 10-11" fill="none" stroke="#3c5fb4" stroke-width="3"/></svg>
    <h4>SUPPLIED</h4><p>We have supplied over 200 expedition-quality aircraft world-wide. We are now manufacturing here in the US.</p>
  </div>
  <div class="rule"></div>
</section>

<section class="timeline">
  <h2>MANUFACTURE TIMELINE</h2>
  <span class="month" style="left:305px">April 2016</span>
  <span class="month" style="left:825px">May 2016</span>
  <svg class="track" viewBox="0 0 1200 50">
    <line x1="40" y1="12" x2="1160" y2="12" stroke="#c9cdd3" stroke-width="2"/>
    <g fill="#3c5fb4">
      <circle cx="100" cy="12" r="5"/><circle cx="170" cy="12" r="5"/><circle cx="220" cy="12" r="5"/>
      <circle cx="315" cy="12" r="5"/><circle cx="360" cy="12" r="5"/><circle cx="410" cy="12" r="5"/>
      <circle cx="480" cy="12" r="5"/><circle cx="545" cy="12" r="5"/><circle cx="650" cy="12" r="5"/>
      <circle cx="700" cy="12" r="5"/><circle cx="800" cy="12" r="5"/><circle cx="965" cy="12" r="5"/>
    </g>
    <circle cx="270" cy="12" r="6" fill="#f2a91c"/>
    <g font-family="Open Sans, sans-serif" font-size="11" fill="#8a929c" text-anchor="middle">
      <text x="100" y="38">1</text><text x="170" y="38">3</text><text x="220" y="38">4</text><text x="270" y="38">5</text>
      <text x="315" y="38">8</text><text x="360" y="38">9</text><text x="410" y="38">11</text><text x="480" y="38">13</text>
      <text x="545" y="38">16</text><text x="650" y="38">19</text><text x="700" y="38">21</text><text x="800" y="38">May 5</text><text x="965" y="38">12</text>
    </g>
  </svg>
  <div class="tl-card" style="left:-30px"><div class="pic" role="img" aria-label="Icon of a packed shipping crate" style="background:#e8b64a"></div><h4>APRIL_5</h4><p>As a market leader in global air freight forwarding, our teams excel in tailored solutions.</p></div>
  <div class="tl-card" style="left:220px"><div class="pic" role="img" aria-label="Icon of a cargo airplane" style="background:#cfd5dc"></div><h4>APRIL_8</h4><p>As a market leader in global air freight forwarding, our teams excel in tailored solutions.</p></div>
  <div class="tl-card" style="left:485px"><div class="pic" role="img" aria-label="Icon of a freight train" style="background:#c9413c"></div><h4>APRIL_11</h4><p>As a market leader in global air freight forwarding, our teams excel in tailored solutions.</p></div>
  <div class="tl-card" style="left:750px"><div class="pic" role="img" aria-label="Icon of a delivery van" style="background:#e8b64a"></div><h4>APRIL_16</h4><p>As a market leader in global air freight forwarding, our teams excel in tailored solutions.</p></div>
  <div class="tl-card" style="left:1010px"><div class="pic" role="img" aria-label="Icon of a globe under a magnifier" style="background:#e08a3c"></div><h4>APRIL_19</h4><p>As a market leader in global air freight forwarding, our teams excel in tailored solutions.</p></div>
  <span class="pager" style="left:520px"></span>
  <span class="pager" style="left:628px"></span>
</section>

<section class="news">
  <h2>FEATURED NEWS</h2>
  <article class="post" style="left:130px"><div class="pic" role="img" aria-label="Photo of a microlight flying over a valley"></div><h3>New Microlight</h3><p>Sed interdum porttitor purus, ut maximus ante luctus quis. Etiam vel vehicula nibh, in malesuada.</p><span class="more">LEARN MORE →</span></article>
  <article class="post" style="left:375px"><div class="pic" role="img" aria-label="Photo of a red microlight in flight"></div><h3>Microlight Freight Forwarding</h3><p>Duis eget dictum eros, in dictum lorem. Vivamus sed molestie sapien. Aliquam et facilisis arcu, et.</p><span class="more">LEARN MORE →</span></article>
  <article class="post" style="left:620px"><div class="pic" role="img" aria-label="Photo of an ultralight above open water"></div><h3>Ultralight Freight Forwarding</h3><p>Sed ac egestas nisl. Sed vestibulum ac diam sit amet porta. Vivamus vel neque, tristique quis.</p><span class="more">LEARN MORE →</span></article>
  <article class="post" style="left:860px"><div class="pic" role="img" aria-label="Photo of a light sport aircraft on a runway"></div><h3>Light Sport</h3><p>Curabitur tristique tempus arcu a placerat. Integer venenatis, magna et lobortis aliquet, diam.</p></article>
</section>

<section class="stats">
  <svg class="rule" viewBox="0 0 940 10"><line x1="5" y1="5" x2="935" y2="5" stroke="#dfe3e8" stroke-width="1.5"/><circle cx="5" cy="5" r="4" fill="#fff" stroke="#c9cdd3"/><circle cx="935" cy="5" r="4" fill="#fff" stroke="#c9cdd3"/></svg>
  <div class="stat" style="left:107px"><div class="stat-num">987</div><span class="stat-label">Aircraft Sold</span></div>
  <div class="stat" style="left:352px"><div class="stat-num">200</div><span class="stat-label">Supplied</span></div>
  <div class="stat" style="left:640px"><div class="stat-num">68</div><span class="stat-label">Current Inventory</span></div>
  <div class="stat" style="left:882px"><div class="stat-num">174</div><span class="stat-label">Different Models</span></div>
</section>

<section class="clients">
  <h2>OUR CLIENTS</h2>
  <span class="client" style="left:195px"></span>
  <span class="client" style="left:365px"></span>
  <span class="client" style="left:540px"></span>
  <span class="client" style="left:715px"></span>
  <span class="client" style="left:885px"></span>
</section>

<section class="contact">
  <div class="vline"></div><div class="dot"></div>
  <h2>CONTACT US</h2>
  <div class="addr"><b>BRISK FERN</b><br>Fernvale, CA 90210, US<br>418 Ridge Rd</div>
  <div class="reach">Tel.: +1 (800) 555 0178<br>e-mail: hello@briskfern.example</div>
  <div class="social"><span></span><span></span><span></span><span></span></div>
  <p class="note">Your email address will not be published. Required fields are marked *</p>
  <div class="field" style="top:130px">Name</div>
  <div class="field" style="top:192px">Email</div>
  <div class="field" style="top:255px">Subject</div>
  <div class="field msg" style="top:318px">Message</div>
  <div class="send">SEND MESSAGE
    <svg width="20" height="16" viewBox="0 0 20 16"><rect x="1" y="1" width="18" height="14" fill="#fff"/><path d="M1 1l9 8 9-8" fill="none" stroke="#223a78" stroke-width="1.6"/></svg>
  </div>
</section>

<footer class="footer">Brisk Fern © 2016 All Rights Reserved. <b>Terms of Use</b> and <b>Privacy Policy</b></footer>

</body>
</html>
```